Vitamin/Dietary Supplement Company needs a simple Hemp CBD Health retail website to display a few...

We need a simple website designed that will allow us to display a few products for purchase. We are a vitamin/dietary supplement company that wants to set up a separate website for CBD health products. CBD is a chemical compound found in hemp and cannabis plants that provide various health and medicinal benefits. Our target audience are individuals that suffer from health issues and would like to treat their pain relief with CBD as an alternative to prescription medication and over the counter drugs such as Paxorin and Dolvex. Looking for a simple and clean website that is easy for customers to navigate and purchase products.

Need extra days to review

Target Market(s)

Our target audience are individuals that suffer from health issues and would like to treat their pain relief with CBD as an alternative to prescription medication and over the counter drugs such as Paxorin and Dolvex.

Coding

Coded - Design and coding required

Font styles to use
Serif

Colors

Designer to choose colors to be used in the design.

Requirements
Nice to have
• Homepage, About page, FAQ page, Contact page, Blog page

```html
<!DOCTYPE html>
<html lang="en">
<head>
<meta charset="utf-8">
<title>Hempwell – CBD Health Products</title>
<link href="https://fonts.googleapis.com/css2?family=Montserrat:wght@400;500;600;700&family=Oswald:wght@500&display=swap" rel="stylesheet">
<style>
:root{
  --green:#566b34;
  --green-dark:#3f5126;
  --green-band:#5b6e3b;
  --ink:#1d1d1d;
  --muted:#7a7a7a;
  --line:#e6e6e6;
  --footer:#0f0f0f;
  --white:#ffffff;
}
*{box-sizing:border-box;margin:0;padding:0}
html,body{width:1200px;height:3871px;overflow:hidden}
body{position:relative;font-family:"Montserrat",sans-serif;color:var(--ink);background:var(--white)}
.abs{position:absolute}
a{color:inherit;text-decoration:none}

/* top bar */
.topbar{left:0;top:0;width:1200px;height:44px;background:var(--green-dark)}
.search{left:78px;top:8px;width:290px;height:28px;border:1px solid rgba(255,255,255,.35);border-radius:14px;color:#dfe5d3;font-size:13px;padding:6px 14px}
.search svg{position:absolute;right:12px;top:6px}
.top-contact{right:80px;top:0;height:44px;display:flex;align-items:center;gap:22px;color:#fff;font-size:14px}
.top-contact span{display:flex;align-items:center;gap:8px}
.icon-dot{width:26px;height:26px;border-radius:50%;background:#fff;display:flex;align-items:center;justify-content:center}

/* header */
.header{left:0;top:44px;width:1200px;height:86px;background:#fff}
.logo{left:78px;top:22px;font-size:28px;font-weight:700;color:var(--green)}
.nav{left:680px;top:0;height:86px;display:flex;align-items:center;gap:34px;font-size:15px;font-weight:500}
.nav .active{position:relative}
.nav .active::after{content:"";position:absolute;left:-14px;right:-14px;bottom:-31px;height:4px;background:var(--green)}
.cart{left:1062px;top:20px}

/* hero */
.hero{left:0;top:130px;width:1200px;height:550px;background:radial-gradient(ellipse at 75% 55%,#9a8d5a 0%,#5e6f3a 35%,#2f3e1e 80%)}
.hero-title{left:0;top:190px;width:1200px;text-align:center;font-family:"Oswald",sans-serif;font-size:50px;color:#fff;letter-spacing:1px}
.hero-sub{left:0;top:256px;width:1200px;text-align:center;font-size:26px;font-weight:600;color:#fff}
.hero-arrow{top:370px;color:#fff}

/* section heads */
.sec-title{font-size:40px;font-weight:600}
.center{left:0;width:1200px;text-align:center}

/* featured */
.feat-img{top:818px;width:333px;height:310px}
.feat-name{top:1152px;width:333px;text-align:center;font-size:15px;font-weight:700}
.feat-desc{top:1180px;width:333px;text-align:center;font-size:13px;color:var(--muted)}
.feat-price{top:1214px;width:333px;text-align:center;font-size:22px;font-weight:600}
.btn-fill{background:var(--green);color:#fff;border-radius:20px;font-size:15px;font-weight:500;display:flex;align-items:center;justify-content:center}
.btn-line{border:2px solid var(--green);color:var(--ink);border-radius:20px;font-size:15px;font-weight:600;display:flex;align-items:center;justify-content:center;background:#fff}
.feat-btn{top:1255px;width:194px;height:40px}
.divider{left:78px;top:1368px;width:1044px;height:1px;background:var(--line)}
.round-arrow{width:40px;height:40px;border-radius:50%;background:#fff;border:1px solid #ddd;box-shadow:0 2px 6px rgba(0,0,0,.15);display:flex;align-items:center;justify-content:center}

/* product cards */
.card{width:249px;height:392px;border:1px solid var(--line);background:#fff}
.card.raised{box-shadow:0 4px 14px rgba(0,0,0,.18);border-color:#eee}
.card-img{position:absolute;left:20px;top:20px;width:209px;height:182px}
.card-name{position:absolute;left:20px;top:218px;font-size:15px;font-weight:700;line-height:26px}
.card-price{position:absolute;left:20px;top:276px;font-size:17px;color:var(--muted);font-weight:500}
.card-stars{position:absolute;left:20px;top:306px;font-size:16px;color:#333;letter-spacing:1px}
.card-stars em{font-style:normal;color:#bbb}
.card-stars small{font-size:12px;color:#aaa;margin-left:16px;letter-spacing:0}
.card-btn{position:absolute;left:20px;top:340px;width:148px;height:40px}

/* about */
.about{left:0;top:2503px;width:1200px;height:415px;background:var(--green-band);color:#fff}
.about h2{position:absolute;left:0;top:62px;width:1200px;text-align:center;font-size:40px;font-weight:600}
.about .lead{position:absolute;left:270px;top:120px;width:660px;text-align:center;font-size:13px;line-height:26px}
.about .body{position:absolute;left:230px;top:176px;width:740px;text-align:center;font-size:13px;line-height:26px;color:#eef1e6}
.about .btn{position:absolute;left:520px;top:330px;width:160px;height:46px;border:2px solid #fff;border-radius:23px;font-size:14px;font-weight:700;display:flex;align-items:center;justify-content:center}

/* blog */
.blog-img{top:3070px;width:333px;height:170px}
.blog-date{top:3206px;width:68px;height:68px;border-radius:50%;background:var(--green);border:4px solid #fff;color:#fff;text-align:center;padding-top:10px}
.blog-date b{display:block;font-size:20px;line-height:22px}
.blog-date span{font-size:11px}
.blog-title{top:3290px;width:333px;font-size:15px;font-weight:700}
.blog-text{top:3318px;width:300px;font-size:13px;line-height:26px;color:var(--muted)}
.blog-more{top:3383px;width:333px;text-align:right;font-size:14px;font-weight:600;text-decoration:underline;color:var(--green)}

/* newsletter */
.news{left:0;top:3462px;width:1200px;height:106px;background:var(--green-band)}
.news h3{position:absolute;left:78px;top:36px;font-size:28px;font-weight:600;color:#fff}
.news .field{position:absolute;left:622px;top:30px;width:500px;height:44px;border-bottom:1px solid rgba(255,255,255,.5);color:#fff;font-size:14px;padding:12px 14px}
.news .sub{position:absolute;left:958px;top:36px;width:162px;height:38px;border-radius:19px;background:#fff;color:var(--green-dark);font-size:15px;font-weight:700;display:flex;align-items:center;justify-content:center}

/* footer */
.footer{left:0;top:3568px;width:1200px;height:303px;background:var(--footer);color:#fff}
.f-logo{position:absolute;left:121px;top:82px;font-size:28px;font-weight:700;color:var(--green)}
.social{position:absolute;left:116px;top:124px;display:flex;gap:7px}
.social i{width:40px;height:40px;border-radius:50%;display:block}
.f-head{position:absolute;top:32px;font-size:15px;font-weight:600;color:var(--green);letter-spacing:1px}
.f-links{position:absolute;left:348px;top:70px;font-size:13px;line-height:29px;color:#ddd;list-style:none}
.f-contact{position:absolute;left:609px;font-size:13px;color:#ddd;display:flex;gap:16px;line-height:20px}
.f-map{position:absolute;left:900px;top:90px;width:190px;height:120px;background:linear-gradient(#1c1c1c,#262626);border-radius:30px 40px 20px 50px;border:1px solid #555}
.f-search{position:absolute;left:950px;top:192px;font-size:13px;color:var(--green);text-decoration:underline}
.f-rule{position:absolute;left:78px;top:238px;width:1044px;height:1px;background:#2e2e2e}
.copy{position:absolute;left:0;top:260px;width:1200px;text-align:center;font-size:13px;color:#ccc}
</style>
</head>
<body>

<div class="abs topbar">
  <div class="abs search">Search ...
    <svg width="16" height="16" viewBox="0 0 16 16" fill="none" stroke="#fff" stroke-width="2"><circle cx="6.5" cy="6.5" r="5"/><path d="M10.5 10.5l4 4"/></svg>
  </div>
  <div class="abs top-contact">
    <span><i class="icon-dot"><svg width="14" height="14" viewBox="0 0 24 24" fill="#3f5126"><path d="M6.6 10.8a15 15 0 006.6 6.6l2.2-2.2c.3-.3.7-.4 1-.2 1.1.4 2.3.6 3.6.6.6 0 1 .4 1 1V20c0 .6-.4 1-1 1A17 17 0 013 4c0-.6.4-1 1-1h3.5c.6 0 1 .4 1 1 0 1.3.2 2.5.6 3.6.1.3 0 .7-.2 1z"/></svg></i>123 456 7890</span>
    <span><i class="icon-dot"><svg width="14" height="14" viewBox="0 0 24 24" fill="#3f5126"><circle cx="12" cy="8" r="5"/><path d="M3 22c0-5 4-8 9-8s9 3 9 8z"/></svg></i>My Account</span>
  </div>
</div>

<header class="abs header">
  <div class="abs logo">Hempwell</div>
  <nav class="abs nav">
    <a class="active">Home</a><a>About</a><a>Faq</a><a>Blog</a><a>Contact</a>
  </nav>
  <svg class="abs cart" width="52" height="44" viewBox="0 0 52 44" fill="none" stroke="#333" stroke-width="2.5">
    <path d="M2 14h40l-5 22H8z"/><path d="M12 14l8-10M32 14l-8-10"/><path d="M14 20v10M22 20v10M30 20v10"/>
    <circle cx="42" cy="10" r="9" fill="#566b34" stroke="none"/>
    <text x="42" y="14" font-size="11" fill="#fff" stroke="none" text-anchor="middle" font-family="Montserrat,sans-serif">0</text>
  </svg>
</header>

<section class="abs hero" role="img" aria-label="Row of green CBD dropper bottles in front of hemp flowers"></section>
<h1 class="abs hero-title">VITAMIN/DIETARY SUPPLEMENT COMPANY</h1>
<p class="abs hero-sub">CBD Health Products</p>
<svg class="abs hero-arrow" style="left:28px" width="20" height="40" viewBox="0 0 20 40" fill="none" stroke="#fff" stroke-width="2"><path d="M16 4L4 20l12 16"/></svg>
<svg class="abs hero-arrow" style="left:1152px" width="20" height="40" viewBox="0 0 20 40" fill="none" stroke="#fff" stroke-width="2"><path d="M4 4l12 16L4 36"/></svg>

<h2 class="abs sec-title center" style="top:732px">Featured Products</h2>

<div class="abs feat-img" style="left:78px;background:linear-gradient(160deg,#c9d3c6,#6f8a4a 70%,#3b4f22)" role="img" aria-label="Amber oil bottles beside hemp leaves"></div>
<div class="abs feat-img" style="left:434px;background:linear-gradient(160deg,#dfe6d8,#2f5b45 55%,#3d3d34)" role="img" aria-label="CBD oil jar on gravel"></div>
<div class="abs feat-img" style="left:789px;background:linear-gradient(160deg,#8a8a58,#5b4a2c 55%,#3a3a24)" role="img" aria-label="Two dropper bottles among dried hemp"></div>

<div class="abs feat-name" style="left:78px">SUPPLEMENT HEMPWELL</div>
<div class="abs feat-name" style="left:434px">SUPPLEMENT HEMPWELL</div>
<div class="abs feat-name" style="left:789px">SUPPLEMENT HEMPWELL</div>
<div class="abs feat-desc" style="left:78px">Lorem ipsum simple text</div>
<div class="abs feat-desc" style="left:434px">Lorem ipsum simple text</div>
<div class="abs feat-desc" style="left:789px">Lorem ipsum simple text</div>
<div class="abs feat-price" style="left:78px">$115.00</div>
<div class="abs feat-price" style="left:434px">$115.00</div>
<div class="abs feat-price" style="left:789px">$115.00</div>
<a class="abs btn-fill feat-btn" style="left:148px">Add To Cart</a>
<a class="abs btn-fill feat-btn" style="left:504px">Add To Cart</a>
<a class="abs btn-fill feat-btn" style="left:859px">Add To Cart</a>

<div class="abs divider"></div>
<div class="abs round-arrow" style="left:560px;top:1348px"><svg width="12" height="12" viewBox="0 0 12 12"><path d="M8 1L2 6l6 5z" fill="#222"/></svg></div>
<div class="abs round-arrow" style="left:610px;top:1348px"><svg width="12" height="12" viewBox="0 0 12 12"><path d="M4 1l6 5-6 5z" fill="#222"/></svg></div>

<!-- Relief products -->
<h2 class="abs sec-title" style="left:78px;top:1438px">Hempwell Products</h2>
<div class="abs round-arrow" style="left:1033px;top:1445px"><svg width="12" height="12" viewBox="0 0 12 12"><path d="M8 1L2 6l6 5z" fill="#222"/></svg></div>
<div class="abs round-arrow" style="left:1082px;top:1445px"><svg width="12" height="12" viewBox="0 0 12 12"><path d="M4 1l6 5-6 5z" fill="#222"/></svg></div>

<div class="abs card raised" style="left:78px;top:1527px">
  <div class="card-img" style="background:radial-gradient(ellipse 30% 48% at 50% 55%,#7fa043,#cfdcb5 70%,#fff 100%)" role="img" aria-label="Green dropper bottle"></div>
  <div class="card-name">DIETARY SUPPLEMENT<br>HEMPWELL</div>
  <div class="card-price">$115.00</div>
  <div class="card-stars">★★★★<em>★</em><small>10 Reviews</small></div>
  <a class="card-btn btn-fill">Add To Cart</a>
</div>
<div class="abs card" style="left:345px;top:1527px">
  <div class="card-img" style="background:radial-gradient(ellipse 30% 48% at 50% 55%,#7fa043,#cfdcb5 70%,#fff 100%)" role="img" aria-label="Green dropper bottle"></div>
  <div class="card-name">DIETARY SUPPLEMENT<br>HEMPWELL</div>
  <div class="card-price">$115.00</div>
  <div class="card-stars">★★★★<em>★</em><small>10 Reviews</small></div>
  <a class="card-btn btn-line">Add To Cart</a>
</div>
<div class="abs card" style="left:612px;top:1527px">
  <div class="card-img" style="background:radial-gradient(ellipse 30% 48% at 50% 55%,#7fa043,#cfdcb5 70%,#fff 100%)" role="img" aria-label="Green dropper bottle"></div>
  <div class="card-name">DIETARY SUPPLEMENT<br>HEMPWELL</div>
  <div class="card-price">$115.00</div>
  <div class="card-stars">★★★★<em>★</em><small>10 Reviews</small></div>
  <a class="card-btn btn-line">Add To Cart</a>
</div>
<div class="abs card" style="left:878px;top:1527px">
  <div class="card-img" style="background:radial-gradient(ellipse 30% 48% at 50% 55%,#7fa043,#cfdcb5 70%,#fff 100%)" role="img" aria-label="Green dropper bottle"></div>
  <div class="card-name">DIETARY SUPPLEMENT<br>HEMPWELL</div>
  <div class="card-price">$115.00</div>
  <div class="card-stars">★★★★<em>★</em><small>10 Reviews</small></div>
  <a class="card-btn btn-line">Add To Cart</a>
</div>

<!-- Gummies -->
<h2 class="abs sec-title" style="left:78px;top:1972px">CBD Gummies</h2>
<div class="abs round-arrow" style="left:1033px;top:1979px"><svg width="12" height="12" viewBox="0 0 12 12"><path d="M8 1L2 6l6 5z" fill="#222"/></svg></div>
<div class="abs round-arrow" style="left:1082px;top:1979px"><svg width="12" height="12" viewBox="0 0 12 12"><path d="M4 1l6 5-6 5z" fill="#222"/></svg></div>

<div class="abs card" style="left:78px;top:2046px">
  <div class="card-img" style="background:radial-gradient(ellipse 38% 50% at 48% 50%,#1f4a2a,#5c8a3a 55%,#f3b06a 72%,#fff 100%)" role="img" aria-label="Pouch of gummy bears"></div>
  <div class="card-name">DIETARY SUPPLEMENT<br>HEMPWELL</div>
  <div class="card-price">$115.00</div>
  <div class="card-stars">★★★★<em>★</em><small>10 Reviews</small></div>
  <a class="card-btn btn-fill">Add To Cart</a>
</div>
<div class="abs card" style="left:345px;top:2046px">
  <div class="card-img" style="background:radial-gradient(ellipse 38% 50% at 48% 50%,#1f4a2a,#5c8a3a 55%,#f3b06a 72%,#fff 100%)" role="img" aria-label="Pouch of gummy bears"></div>
  <div class="card-name">DIETARY SUPPLEMENT<br>HEMPWELL</div>
  <div class="card-price">$115.00</div>
  <div class="card-stars">★★★★<em>★</em><small>10 Reviews</small></div>
  <a class="card-btn btn-line">Add To Cart</a>
</div>
<div class="abs card" style="left:612px;top:2046px">
  <div class="card-img" style="background:radial-gradient(ellipse 38% 50% at 48% 50%,#1f4a2a,#5c8a3a 55%,#f3b06a 72%,#fff 100%)" role="img" aria-label="Pouch of gummy bears"></div>
  <div class="card-name">DIETARY SUPPLEMENT<br>HEMPWELL</div>
  <div class="card-price">$115.00</div>
  <div class="card-stars">★★★★<em>★</em><small>10 Reviews</small></div>
  <a class="card-btn btn-line">Add To Cart</a>
</div>
<div class="abs card" style="left:878px;top:2046px">
  <div class="card-img" style="background:radial-gradient(ellipse 38% 50% at 48% 50%,#1f4a2a,#5c8a3a 55%,#f3b06a 72%,#fff 100%)" role="img" aria-label="Pouch of gummy bears"></div>
  <div class="card-name">DIETARY SUPPLEMENT<br>HEMPWELL</div>
  <div class="card-price">$115.00</div>
  <div class="card-stars">★★★★<em>★</em><small>10 Reviews</small></div>
  <a class="card-btn btn-line">Add To Cart</a>
</div>

<!-- About -->
<section class="abs about">
  <h2>About Hempwell</h2>
  <p class="lead">CBD is a chemical compound found in hemp and cannabis plants that provide various health and medicinal benefits</p>
  <p class="body">Lorem Ipsum is simply dummy text of the printing and typesetting industry. Lorem Ipsum has been the industry's standard dummy text ever since the 1500s, when an unknown printer took a galley of type and scrambled it to make a type specimen book. It has survived not only five centuries, but also the leap into electronic typesetting, remaining essentially unchanged. It was popula</p>
  <a class="btn">LEARN MORE</a>
</section>

<!-- Blog -->
<h2 class="abs sec-title center" style="top:2978px">Latest Blog</h2>
<div class="abs blog-img" style="left:78px;background:linear-gradient(135deg,#4f6a2c,#8da25a 50%,#2f3f1c)" role="img" aria-label="Dropper bottle among hemp buds"></div>
<div class="abs blog-img" style="left:434px;background:linear-gradient(120deg,#6b6b6b,#b09a88 55%,#4a4a4a)" role="img" aria-label="Person holding a sore neck"></div>
<div class="abs blog-img" style="left:789px;background:linear-gradient(120deg,#f2f2ee,#c9a24a 45%,#5d7a30)" role="img" aria-label="Oil vial with hemp leaves"></div>

<div class="abs blog-date" style="left:90px"><b>12</b><span>Dec</span></div>
<div class="abs blog-date" style="left:446px"><b>12</b><span>Dec</span></div>
<div class="abs blog-date" style="left:801px"><b>12</b><span>Dec</span></div>

<div class="abs blog-title" style="left:90px">Lorem ipsum type text of print industry.</div>
<div class="abs blog-title" style="left:446px">Lorem ipsum type text of print industry.</div>
<div class="abs blog-title" style="left:809px">Lorem ipsum type text of print industry.</div>
<div class="abs blog-text" style="left:90px">Lorem Ipsum is simply dummy text of the print ing and typesetting industry Lorem.</div>
<div class="abs blog-text" style="left:446px">Lorem Ipsum is simply dummy text of the print ing and typesetting industry Lorem.</div>
<div class="abs blog-text" style="left:809px">Lorem Ipsum is simply dummy text of the print ing and typesetting industry Lorem.</div>
<a class="abs blog-more" style="left:78px">Read More..»</a>
<a class="abs blog-more" style="left:434px">Read More..»</a>
<a class="abs blog-more" style="left:789px">Read More..»</a>

<!-- Newsletter -->
<section class="abs news">
  <h3>Sign Up For Newsletter</h3>
  <div class="field">Enter Email*</div>
  <a class="sub">SUBSCRIBE</a>
</section>

<!-- Footer -->
<footer class="abs footer">
  <div class="f-logo">Hempwell</div>
  <div class="social">
    <i style="background:#3b5998"></i><i style="background:#1da1f2"></i><i style="background:#0e76a8"></i><i style="background:#c4302b"></i>
  </div>

  <div class="f-head" style="left:348px">SITEMAP</div>
  <ul class="f-links"><li>Home</li><li>About</li><li>Faq</li><li>Blog</li><li>Contact</li></ul>

  <div class="f-head" style="left:609px">CONTACT US</div>
  <div class="f-contact" style="top:76px">
    <svg width="16" height="22" viewBox="0 0 16 22" fill="#8aa05a"><path d="M8 0a8 8 0 00-8 8c0 6 8 14 8 14s8-8 8-14a8 8 0 00-8-8zm0 11a3 3 0 110-6 3 3 0 010 6z"/></svg>
    <span>101 - Lorem ipsum simple text<br>of print industry.</span>
  </div>
  <div class="f-contact" style="top:134px">
    <svg width="16" height="16" viewBox="0 0 24 24" fill="#8aa05a"><path d="M6.6 10.8a15 15 0 006.6 6.6l2.2-2.2c.3-.3.7-.4 1-.2 1.1.4 2.3.6 3.6.6.6 0 1 .4 1 1V20c0 .6-.4 1-1 1A17 17 0 013 4c0-.6.4-1 1-1h3.5c.6 0 1 .4 1 1 0 1.3.2 2.5.6 3.6.1.3 0 .7-.2 1z"/></svg>
    <span>123 456 7890</span>
  </div>
  <div class="f-contact" style="top:170px">
    <svg width="18" height="14" viewBox="0 0 18 14" fill="none" stroke="#8aa05a" stroke-width="2"><rect x="1" y="1" width="16" height="12"/><path d="M1 1l8 7 8-7"/></svg>
    <span>info@hempwell.com</span>
  </div>

  <div class="f-head" style="left:877px">LOCATION MAP</div>
  <div class="f-map" role="img" aria-label="Outline map of the United States"></div>
  <a class="f-search">Search Here</a>

  <div class="f-rule"></div>
  <p class="copy">©Hempwell - 2018 All Right Reserved.</p>
</footer>

</body>
</html>
```